Beautiful Quotes For Social Media Posts

We are looking for 5 beautifully designed quotes for our social media account.

Inspiration of styles we like in both style and color along with a few of our favorite fonts (you are NOT limited to these fonts this is just to give you an idea):
https://quillmorestudio.example.com/s/k7p2vx9tqa41mzn8wbd3ce6hr5lf0y2j

*These fonts are property of Quillmore Studio. You do not have permission/rights to use them outside of this assignment*

Quotes to use (5):
“Only those who dare to fail greatly can ever achieve greatly.” –Vernon T. Ashgrove
“Don’t go through life, grow through life.” – Milo Pendrake
“Follow your bliss and the universe will open doors where there were only walls.” – Arthur Venholm
“If you don’t like the road you’re walking, start paving another one.” – Greta Mossley
“Life is like riding a bicycle. To keep your balance, you must keep moving.” —Lucian Thornwick

File Specifics:
- JPG
- 10x10 in size (square)
- Please include @QuillmoreStudio in the bottom right left or center of each design

Brand Details:
Soft but rich pastel and bright colors.
Hand Drawn florals, doodles and art
Handwritten looking fonts
Artsy, Creative, Girl and Inspiring

```html
<!DOCTYPE html>
<html lang="en">
<head>
<meta charset="utf-8">
<title>Grow Through Life – Quote Post</title>
<link rel="stylesheet" href="https://fonts.googleapis.com/css2?family=Amatic+SC:wght@700&family=Source+Sans+3:wght@400&display=swap">
<style>
  :root {
    --white: #ffffff;
    --sage: #c5cbbf;
    --blush: #e7a0a8;
    --rose: #e48d9b;
    --ink: #5d5d5d;
  }
  html, body {
    margin: 0;
    padding: 0;
    overflow: hidden;
  }
  .post {
    position: relative;
    width: 1200px;
    height: 1200px;
    overflow: hidden;
    background: repeating-linear-gradient(
      135deg,
      var(--white) 0 104px,
      var(--sage) 104px 182px
    );
  }
  .scatter {
    position: absolute;
    inset: 0;
    width: 1200px;
    height: 1200px;
  }
  .scatter .dot { fill: var(--rose); }
  .scatter .star-mark { fill: var(--rose); opacity: 0.55; }

  .quote-card {
    position: absolute;
    left: 260px;
    top: 269px;
    width: 672px;
    height: 655px;
    background: var(--white);
    border: 3px solid var(--blush);
  }
  .quote-panel {
    position: absolute;
    left: 51px;
    top: 48px;
    width: 572px;
    height: 558px;
    background: var(--blush);
  }
  .quote-panel svg {
    position: absolute;
    inset: 0;
    width: 572px;
    height: 558px;
  }
  .quote-panel .sparkle { fill: var(--white); }
  .quote-text {
    position: absolute;
    inset: 0;
    margin: 0;
    font-family: "Amatic SC", cursive;
    font-weight: 700;
    color: var(--white);
    font-size: 98px;
    text-transform: uppercase;
    text-align: center;
    letter-spacing: 3px;
  }
  .quote-line {
    position: absolute;
    left: 0;
    right: 0;
    line-height: 1;
    white-space: nowrap;
  }
  .line-1 { top: 28px; }
  .line-2 { top: 168px; }
  .line-3 { top: 306px; }
  .line-4 { top: 444px; }

  .quote-author {
    position: absolute;
    right: 20px;
    bottom: 10px;
    margin: 0;
    font-family: "Source Sans 3", sans-serif;
    font-size: 24px;
    color: var(--ink);
  }

  .handle {
    position: absolute;
    left: 0;
    right: 0;
    bottom: 24px;
    margin: 0;
    text-align: center;
    font-family: "Source Sans 3", sans-serif;
    font-size: 20px;
    line-height: 24px;
    color: var(--ink);
  }
</style>
</head>
<body>
  <main class="post">
    <svg class="scatter" viewBox="0 0 1000 1000">
      <g class="confetti-dots">
        <circle class="dot" cx="183" cy="43" r="4"/>
        <circle class="dot" cx="156" cy="103" r="7"/>
        <circle class="dot" cx="626" cy="59" r="7"/>
        <circle class="dot" cx="780" cy="118" r="7"/>
        <circle class="dot" cx="848" cy="278" r="7"/>
        <circle class="dot" cx="884" cy="438" r="7"/>
        <circle class="dot" cx="930" cy="632" r="7"/>
        <circle class="dot" cx="834" cy="932" r="7"/>
      </g>
      <g class="star-doodles" role="img" aria-label="Scattered hand-drawn pink outline stars">
        <circle class="star-mark" cx="80" cy="135" r="9"/>
        <circle class="star-mark" cx="535" cy="145" r="13"/>
        <circle class="star-mark" cx="945" cy="145" r="13"/>
        <circle class="star-mark" cx="80" cy="380" r="9"/>
        <circle class="star-mark" cx="80" cy="590" r="13"/>
        <circle class="star-mark" cx="948" cy="588" r="13"/>
        <circle class="star-mark" cx="80" cy="790" r="9"/>
        <circle class="star-mark" cx="693" cy="848" r="9"/>
        <circle class="star-mark" cx="232" cy="888" r="8"/>
        <circle class="star-mark" cx="460" cy="888" r="9"/>
        <circle class="star-mark" cx="205" cy="915" r="8"/>
        <circle class="star-mark" cx="868" cy="893" r="9"/>
      </g>
    </svg>

    <section class="quote-card">
      <div class="quote-panel">
        <svg viewBox="0 0 572 558">
          <g class="sparkles">
            <circle class="sparkle" cx="44" cy="35" r="4"/>
            <circle class="sparkle" cx="32" cy="48" r="4"/>
            <circle class="sparkle" cx="116" cy="149" r="4"/>
            <circle class="sparkle" cx="541" cy="77" r="4"/>
            <circle class="sparkle" cx="429" cy="120" r="4"/>
            <circle class="sparkle" cx="87" cy="400" r="4"/>
            <circle class="sparkle" cx="493" cy="432" r="4"/>
            <circle class="sparkle" cx="54" cy="475" r="4"/>
          </g>
          <g class="heart-doodles" role="img" aria-label="Small white hand-drawn hearts">
            <circle class="sparkle" cx="441" cy="77" r="9"/>
            <circle class="sparkle" cx="72" cy="364" r="9"/>
            <circle class="sparkle" cx="490" cy="389" r="9"/>
          </g>
        </svg>
        <blockquote class="quote-text">
          <span class="quote-line line-1">Don’t</span>
          <span class="quote-line line-2">Go through life</span>
          <span class="quote-line line-3">Grow</span>
          <span class="quote-line line-4">through life</span>
        </blockquote>
      </div>
      <p class="quote-author">Milo Pendrake</p>
    </section>

    <p class="handle">@QuillmoreStudio</p>
  </main>
</body>
</html>
```